Brochure for software platform

We need a clean and professional brochure (max 4 pages) for one of our products called "Tallyp.io", see https://tallyp.io/en. The product is a software platform to manage the application and selection process for grants, awards or similar challenges. Our company is called Brentmoor Systems AG and we are based in Switzerland. The brochure should be in English but might be translated into German. The design should be based on the information provided on the website and in the presentation available on google drive (with logo,...). See
https://files.quorvex-share.net/folders/8KdPq27LmWzRt5vNx3aYc-h41JbUEsTfG?usp=sharing
Additional screenshots for mockups can be provided once closer to the final design. Design should be clean and professional.

Target Market(s)

Foundations, Investors, Accelerators, Award organisers

Font styles to use
Other font styles liked:
• Opens Sans Light

Colors
0492cd
34a6d7
85cae6
0255a3
3377b5

Requirements
Must have
• Use white (or bright) background. And the blue logo color for font titles. At least one mockup with a screenshot of the platform (see website). No must of customer logos but if it fits we can provide some (see as on website).

```html
<!DOCTYPE html>
<html lang="en">
<head>
<meta charset="utf-8">
<title>Tallyp brochure</title>
<link rel="stylesheet" href="https://fonts.googleapis.com/css2?family=Open+Sans:wght@300;400;600&display=swap">
<style>
:root{
  --blue:#0492cd;
  --blue-mid:#34a6d7;
  --blue-soft:#85cae6;
  --blue-deep:#0255a3;
  --blue-steel:#3377b5;
  --cover:#6aaee0;
  --title:#4a9ad8;
  --ink:#222;
  --grey:#555;
  --paper:#fff;
  --backdrop:#e9e9e9;
}
*{box-sizing:border-box;margin:0;padding:0}
html,body{width:1200px;height:922px;overflow:hidden}
body{background:var(--backdrop);font-family:"Open Sans",Arial,sans-serif;font-weight:300;color:var(--ink);position:relative}
.page{position:absolute;width:543px;background:var(--paper);overflow:hidden}
.spread-top .page{top:55px;height:382px}
.spread-bottom .page{top:475px;height:383px}
.p-left{left:50px}
.p-right{left:593px}

.wordmark{display:flex;align-items:center;gap:12px;font-weight:400;letter-spacing:1px;line-height:1}
.wordmark .dot{border-radius:50%;flex:none}

/* back cover */
.back-cover{background:var(--cover)}
.back-cover .wordmark{position:absolute;left:0;right:0;top:158px;justify-content:center;color:#fff;font-size:54px}
.back-cover .wordmark .dot{width:40px;height:40px;background:#fff}
.back-cover .tagline{position:absolute;top:249px;left:0;right:0;text-align:center;color:#fff;font-size:11.5px;line-height:14px}
.social{position:absolute;top:297px;left:0;right:0;display:flex;justify-content:center;gap:10px}
.social span{width:21px;height:21px;border:1.5px solid #fff;border-radius:50%}
.contact-bar{position:absolute;left:0;right:0;top:338px;height:29px;background:#f3f3f3;display:flex;align-items:center;justify-content:space-around;font-size:12px;color:var(--grey)}
.contact-bar .item{display:flex;align-items:center;gap:7px}
.contact-bar svg{width:13px;height:13px}

/* front cover */
.front-cover .wordmark{position:absolute;left:29px;top:95px;color:var(--title);font-size:55px}
.front-cover .wordmark .dot{width:40px;height:40px;background:var(--title)}
.front-cover .headline{position:absolute;left:29px;top:188px;font-size:18px;line-height:27px;color:#333;letter-spacing:.5px}
.front-cover .url{position:absolute;left:29px;top:300px;font-size:18px;color:var(--title)}
.front-cover .art{position:absolute;inset:0}

/* inside left */
.intro-hero{position:absolute;left:0;top:0;width:543px;height:180px}
.intro-hero .wordmark{position:absolute;left:0;right:0;top:52px;justify-content:center;color:#fff;font-size:54px}
.intro-hero .wordmark .dot{width:40px;height:40px;background:#fff}
.intro-text{position:absolute;top:203px;width:248px;font-size:11.5px;line-height:14px;text-align:justify}
.intro-text p{position:relative;padding-left:19px;margin-bottom:16px}
.intro-text p svg{position:absolute;left:0;top:1px;width:12px;height:12px}
.col-a{left:14px}
.col-b{left:274px}

/* features */
.features{position:absolute;inset:0}
.feature{position:absolute;font-size:9.5px;line-height:11px;color:var(--ink);text-align:justify}
.feature h3{font-weight:300;font-size:12px;line-height:13px;color:var(--title);margin-bottom:4px;text-align:left}
.f-forms{left:54px;top:46px;width:218px}
.f-support{left:287px;top:46px;width:196px}
.f-ui{left:34px;top:148px;width:110px;text-align:left}
.f-hosting{left:401px;top:148px;width:110px}
.f-messaging{left:54px;top:302px;width:218px}
.f-infra{left:287px;top:302px;width:192px}
</style>
</head>
<body>

<div class="spread-top">
  <section class="page p-left back-cover">
    <div class="wordmark"><span class="dot"></span>tallyp</div>
    <p class="tagline">An intuitive platform for efficiently managing the application,<br>review and selection process for challenges and awards.</p>
    <div class="social" aria-label="Social channels"><span></span><span></span><span></span><span></span><span></span></div>
    <div class="contact-bar">
      <div class="item"><svg viewBox="0 0 14 14"><circle cx="7" cy="7" r="7" fill="var(--title)"/><rect x="3.5" y="4.5" width="7" height="5" fill="none" stroke="#fff" stroke-width="1"/><path d="M3.5 4.5 7 7.5 10.5 4.5" fill="none" stroke="#fff" stroke-width="1"/></svg>m.ostrander@brentmoorsystems.ch</div>
      <div class="item"><svg viewBox="0 0 14 14"><circle cx="7" cy="7" r="7" fill="var(--title)"/><path d="M5 3.5c-1 1-1 3 1 5s4 2 5 1l-1.5-1.5-1 .7c-.8-.3-1.9-1.4-2.2-2.2l.7-1z" fill="#fff"/></svg>+41 79 555 01 27</div>
      <div class="item"><svg viewBox="0 0 14 14"><circle cx="7" cy="7" r="7" fill="var(--title)"/><circle cx="7" cy="7" r="3.8" fill="none" stroke="#fff" stroke-width=".9"/><path d="M3.2 7h7.6M7 3.2v7.6" stroke="#fff" stroke-width=".9"/></svg>www.tallyp.io</div>
    </div>
  </section>

  <section class="page p-right front-cover">
    <svg class="art" viewBox="0 0 543 382" width="543" height="382">
      <polygon points="222,0 543,0 543,382 355,382" fill="#8d8d8d" role="img" aria-label="Black and white photo of a speaker addressing a conference audience"/>
      <polygon points="213,382 380,382 300,300" fill="var(--title)"/>
      <g role="img" aria-label="Desktop monitor showing the platform's application list screen">
        <rect x="251" y="193" width="228" height="148" rx="4" fill="#111"/>
        <rect x="256" y="198" width="218" height="137" fill="#fafafa"/>
        <rect x="256" y="198" width="28" height="137" fill="#2b2b2b"/>
        <path d="M350 341h30l6 22h-42z" fill="#bfbfbf"/>
        <rect x="330" y="362" width="70" height="6" rx="3" fill="#9a9a9a"/>
      </g>
    </svg>
    <div class="wordmark"><span class="dot"></span>tallyp</div>
    <p class="headline">DIGITAL<br>APPLICATION<br>MANAGEMENT</p>
    <p class="url">www.tallyp.io</p>
  </section>
</div>

<div class="spread-bottom">
  <section class="page p-left">
    <div class="intro-hero">
      <svg width="543" height="180" viewBox="0 0 543 180" role="img" aria-label="Blue-tinted photo of a presenter in front of a conference audience">
        <defs><linearGradient id="heroTint" x1="0" x2="1"><stop offset="0" stop-color="#8db8e0"/><stop offset="1" stop-color="#6f9fd0"/></linearGradient></defs>
        <polygon points="0,0 543,0 543,157 310,157 297,170 284,157 0,157" fill="url(#heroTint)"/>
      </svg>
      <div class="wordmark"><span class="dot"></span>tallyp</div>
    </div>
    <div class="intro-text col-a">
      <p><svg viewBox="0 0 12 12"><path d="M2 6.5 5 9.5 10.5 2.5" fill="none" stroke="var(--title)" stroke-width="2"/></svg>Tallyp is a fully customized and intuitive platform to efficiently manage the application, revision and selection process for grants, investments, accelerators and awards.</p>
      <p><svg viewBox="0 0 12 12"><path d="M2 6.5 5 9.5 10.5 2.5" fill="none" stroke="var(--title)" stroke-width="2"/></svg>Fully customized process<br>Applications are accepted, revised and selected through a branded web portal. The revision and selection workflow is fully tailored. Integrated messaging allows frictionless communication.</p>
    </div>
    <div class="intro-text col-b">
      <p><svg viewBox="0 0 12 12"><path d="M2 6.5 5 9.5 10.5 2.5" fill="none" stroke="var(--title)" stroke-width="2"/></svg>Tallyp can be licensed with different monthly plans available. All plans include custom branding and configuration, hosting and support.</p>
      <p><svg viewBox="0 0 12 12"><path d="M2 6.5 5 9.5 10.5 2.5" fill="none" stroke="var(--title)" stroke-width="2"/></svg>The tallyp application management platform is a modern and intuitive platform to digitize and streamline the application and revision process.</p>
    </div>
  </section>

  <section class="page p-right">
    <svg class="features" viewBox="0 0 543 383" width="543" height="383">
      <g fill="none" stroke="var(--title)" stroke-width="1.3">
        <path d="M34 68V131H193"/><path d="M508 68V131H352"/>
        <path d="M34 318V237H193"/><path d="M508 318V237H352"/>
        <path d="M150 185H193"/><path d="M352 185H396"/>
      </g>
      <g fill="var(--title)">
        <circle cx="193" cy="131" r="3"/><circle cx="352" cy="131" r="3"/>
        <circle cx="193" cy="237" r="3"/><circle cx="352" cy="237" r="3"/>
        <circle cx="193" cy="185" r="3"/><circle cx="352" cy="185" r="3"/>
      </g>
      <g>
        <circle cx="34" cy="53" r="15" fill="var(--title)" stroke="#d6e8f6" stroke-width="3"/>
        <rect x="27" y="46" width="14" height="14" fill="none" stroke="#fff" stroke-width="1.4"/>
        <circle cx="508" cy="53" r="15" fill="var(--title)" stroke="#d6e8f6" stroke-width="3"/>
        <circle cx="508" cy="49" r="4" fill="#fff"/><path d="M501 61a7 6 0 0 1 14 0z" fill="#fff"/>
        <circle cx="34" cy="318" r="15" fill="var(--title)" stroke="#d6e8f6" stroke-width="3"/>
        <rect x="26" y="311" width="16" height="11" rx="4" fill="#fff"/>
        <circle cx="508" cy="318" r="15" fill="var(--title)" stroke="#d6e8f6" stroke-width="3"/>
        <rect x="501" y="312" width="14" height="9" fill="none" stroke="#fff" stroke-width="1.4"/><path d="M499 324h18" stroke="#fff" stroke-width="1.4"/>
      </g>
      <g role="img" aria-label="Desktop monitor showing the platform's application overview screen">
        <rect x="168" y="121" width="204" height="124" rx="5" fill="#111"/>
        <rect x="173" y="126" width="194" height="113" fill="#fafafa"/>
        <rect x="173" y="126" width="26" height="113" fill="#2b2b2b"/>
        <path d="M256 245h32l6 30h-44z" fill="#bdbdbd"/>
        <rect x="240" y="274" width="64" height="6" rx="3" fill="#999"/>
      </g>
    </svg>
    <div class="feature f-forms"><h3>Structured application forms</h3>Application data is collected through web forms with dedicated field types, display logic and input validation.</div>
    <div class="feature f-support"><h3>Dedicated support</h3>Dedicated service contracts for tailored and personal customer support.</div>
    <div class="feature f-ui"><h3>Customised user interface</h3>The user interface is custom branded and intuitive. Applicants are guided through the submission process.</div>
    <div class="feature f-hosting"><h3>Secure hosting and transmission</h3>Hosted in Swiss ISO and CFRB certified data center. Encrypted transmission.</div>
    <div class="feature f-messaging"><h3>Integrated messaging</h3>Messaging functionalities within the platform allow frictionless communication with all or individual users</div>
    <div class="feature f-infra"><h3>Reliable infrastructure</h3>Guaranteed infrastructure uptime of 99.9 % with scheduled maintenance windows.</div>
  </section>
</div>

</body>
</html>
```